Oven Cleaning flyer design

Hi there,
I need help designing a letterbox flyer. It needs to be DL size.
I have attached a rough design made with Chat GPT.
Would like back and front, have my business colors.
Please find attached mock up of what I would roughly like.
Also find attached logo.
Thank you

Target Market(s)

Home owners over 40

Industry/Entity Type

Cleaning

Requirements
Must have
• Logo, before after of oven, brand colors

```html
<!DOCTYPE html>
<html lang="en">
<head>
<meta charset="utf-8">
<title>Gleam Oven Care – DL Flyer</title>
<link href="https://fonts.googleapis.com/css2?family=Krona+One&family=Nunito:wght@500;600;700&display=swap" rel="stylesheet">
<style>
  :root{
    --teal:#4bc1c9;
    --ink:#111111;
    --paper:#ffffff;
    --stage:#2f2f2f;
    --display:"Krona One", sans-serif;
    --body:"Nunito", sans-serif;
  }
  *{box-sizing:border-box;margin:0;padding:0}
  html,body{width:1200px;height:1178px;overflow:hidden;background:var(--stage)}
  .canvas{position:relative;width:1200px;height:1178px}
  .flyer{position:absolute;top:199px;width:379px;height:780px;background:var(--paper);overflow:hidden;color:var(--ink)}
  .flyer--front{left:212px}
  .flyer--back{left:609px}
  .abs{position:absolute;left:0;right:0;text-align:center;white-space:nowrap}

  .brand{position:absolute;left:0;right:0;display:flex;align-items:center;justify-content:center;gap:9px}
  .brand__dot{width:30px;height:30px;border-radius:50%;background:var(--teal)}
  .brand__name{font-family:var(--display);font-size:15px;color:var(--teal);letter-spacing:.5px}
  .flyer--back .brand__dot{background:var(--paper)}
  .flyer--back .brand__name{color:var(--paper)}

  .display{font-family:var(--display)}
  .teal{color:var(--teal)}

  .photo{position:absolute}
  .photo--before{background:linear-gradient(160deg,#3a2a1c 0%,#6a4a26 45%,#2a2118 100%)}
  .photo--after{background:linear-gradient(160deg,#3d3a38 0%,#7a7570 50%,#2d2b2a 100%)}
  .tag{position:absolute;font-family:var(--body);font-weight:700;font-size:13px;display:flex;align-items:center;justify-content:center}

  .icon{display:inline-block;vertical-align:middle}

  .teal-head{position:absolute;left:0;top:0;width:379px;height:231px;background:var(--teal)}
  .lede{position:absolute;left:20px;right:20px;text-align:center;font-family:var(--body);font-weight:500;font-size:10px;line-height:14px;color:var(--paper)}

  .checks{position:absolute;left:30px;top:513px;list-style:none}
  .checks li{display:flex;align-items:center;gap:10px;height:28.5px;font-family:var(--body);font-weight:600;font-size:18px}
  .deco-circle{position:absolute;left:292px;top:522px;width:50px;height:50px;border-radius:50%;background:var(--teal);opacity:.25}

  .contact-band{position:absolute;left:0;top:611px;width:379px;height:85px;background:var(--ink);color:var(--paper)}
</style>
</head>
<body>
<div class="canvas">

  <!-- FRONT -->
  <section class="flyer flyer--front">
    <div class="brand" style="top:36px">
      <span class="brand__dot"></span><span class="brand__name">GLEAM OVEN CARE</span>
    </div>

    <div class="abs display teal" style="top:97px;font-size:21.5px">BRING YOUR OVEN</div>
    <div class="abs display" style="top:121px;font-size:30px">BACK TO LIFE</div>
    <p class="abs display" style="top:164px;font-size:8.6px;line-height:13px;white-space:normal;padding:0 36px">Professional, non-caustic oven cleaning that removes built-up grease, smoke, and bunt grime - leaving your oven looking fresh again.</p>

    <div class="photo photo--before" style="left:0;top:226px;width:196px;height:394px" role="img" aria-label="Dirty oven interior with greasy racks and stained glass door before cleaning"></div>
    <div class="photo photo--after" style="left:198px;top:226px;width:181px;height:394px" role="img" aria-label="Clean oven interior with shiny racks and clear glass door after cleaning"></div>
    <div class="tag" style="left:0;top:226px;width:110px;height:30px;background:var(--teal);color:var(--paper)">BEFORE</div>
    <div class="tag" style="left:283px;top:226px;width:96px;height:32px;background:var(--ink);color:var(--paper)">AFTER</div>

    <div class="abs display teal" style="top:644px;font-size:28px">CALL NOW FOR</div>
    <div class="abs display" style="top:681px;font-size:13.5px">FAST, PROFESSIONAL SERVICE</div>
    <div class="abs display" style="top:711px;font-size:23px">
      <svg class="icon" width="15" height="15" viewBox="0 0 16 16"><circle cx="8" cy="8" r="8" fill="var(--teal)"/><path d="M5.2 4.2l1.6 0 .6 1.8-1 .8c.5 1.1 1.3 1.9 2.4 2.4l.8-1 1.8.6 0 1.6c-3.5.4-6.6-2.7-6.2-6.2z" fill="#fff"/></svg>
      0400 123 987
    </div>
    <div class="abs display" style="top:740px;font-size:12.5px">
      <svg class="icon" width="14" height="14" viewBox="0 0 16 16"><circle cx="8" cy="8" r="8" fill="var(--teal)"/><circle cx="8" cy="8" r="4.5" fill="none" stroke="#fff"/><path d="M3.5 8h9M8 3.5c-2 2.5-2 6.5 0 9M8 3.5c2 2.5 2 6.5 0 9" fill="none" stroke="#fff" stroke-width=".8"/></svg>
      GLEAMOVENCARE.COM.AU
    </div>
  </section>

  <!-- BACK -->
  <section class="flyer flyer--back">
    <div class="teal-head"></div>
    <div class="brand" style="top:36px">
      <span class="brand__dot"></span><span class="brand__name">GLEAM OVEN CARE</span>
    </div>

    <div class="abs display" style="top:95px;font-size:20px;color:var(--paper)">WHY CHOOSE</div>
    <div class="abs display" style="top:120px;font-size:11.5px">GLEAM OVEN CARE?</div>
    <svg class="abs" style="top:140px;margin:0 auto;left:0;right:0" width="42" height="8" viewBox="0 0 42 8"><line x1="0" y1="4" x2="42" y2="4" stroke="#fff" stroke-width="1"/><circle cx="21" cy="4" r="2.5" fill="#fff"/></svg>
    <p class="lede" style="top:157px">We're a local family business providing professional, non-caustic oven cleaning across Sunshine Coast. Using specialized-equipment and proven cleaning methods, we remove heavy grease, carbon build-up, smoke residue, restoring your oven safely and effectively.</p>

    <div class="photo photo--before" style="left:0;top:231px;width:183px;height:197px" role="img" aria-label="Greasy oven interior with dark stained back wall before cleaning"></div>
    <div class="photo photo--after" style="left:186px;top:231px;width:193px;height:197px" role="img" aria-label="Bright clean oven interior with polished racks after cleaning"></div>
    <div class="tag" style="left:0;top:231px;width:97px;height:27px;background:var(--paper);color:var(--ink)">BEFORE</div>
    <div class="tag" style="left:271px;top:231px;width:108px;height:28px;background:var(--paper);color:var(--ink)">AFTER</div>

    <div class="abs display" style="top:455px;font-size:16.5px">MENTION THIS FLYER FOR</div>
    <div class="abs display" style="top:474px;font-size:12.5px">
      <span class="teal" style="font-size:22px;vertical-align:-2px">$10 OFF</span> YOUR FIRST CLEAN
    </div>

    <ul class="checks">
      <li><svg width="17" height="17" viewBox="0 0 18 18"><circle cx="9" cy="9" r="7.5" fill="none" stroke="var(--teal)" stroke-width="1.6"/><path d="M5.5 9l2.5 2.5L15 4" fill="none" stroke="var(--teal)" stroke-width="1.8"/></svg>Reliable Service</li>
      <li><svg width="17" height="17" viewBox="0 0 18 18"><circle cx="9" cy="9" r="7.5" fill="none" stroke="var(--teal)" stroke-width="1.6"/><path d="M5.5 9l2.5 2.5L15 4" fill="none" stroke="var(--teal)" stroke-width="1.8"/></svg>Non-Caustic Cleaning</li>
      <li><svg width="17" height="17" viewBox="0 0 18 18"><circle cx="9" cy="9" r="7.5" fill="none" stroke="var(--teal)" stroke-width="1.6"/><path d="M5.5 9l2.5 2.5L15 4" fill="none" stroke="var(--teal)" stroke-width="1.8"/></svg>Satisfaction Guaranteed</li>
    </ul>
    <div class="deco-circle"></div>

    <div class="contact-band">
      <div class="abs display" style="top:13px;font-size:26px">
        <svg class="icon" width="17" height="17" viewBox="0 0 16 16"><circle cx="8" cy="8" r="8" fill="#fff"/><path d="M5.2 4.2l1.6 0 .6 1.8-1 .8c.5 1.1 1.3 1.9 2.4 2.4l.8-1 1.8.6 0 1.6c-3.5.4-6.6-2.7-6.2-6.2z" fill="var(--ink)"/></svg>
        0400 123 987
      </div>
      <div class="abs display" style="top:54px;font-size:14px">
        <svg class="icon" width="16" height="16" viewBox="0 0 16 16"><circle cx="8" cy="8" r="8" fill="#fff"/><circle cx="8" cy="8" r="4.5" fill="none" stroke="var(--ink)"/><path d="M3.5 8h9M8 3.5c-2 2.5-2 6.5 0 9M8 3.5c2 2.5 2 6.5 0 9" fill="none" stroke="var(--ink)" stroke-width=".8"/></svg>
        GLEAMOVENCARE.COM.AU
      </div>
    </div>

    <div class="abs display" style="top:715px;font-size:15px;line-height:21px">WE ALSO CLEAN COOKTOPS,<br>RANGEHOODS AND BBQS</div>
  </section>

</div>
</body>
</html>
```